Maine Organic farm needs a label design for various food products

We need a label design that we can use across a variety of vegetable-based food products that we produce using some of our organic vegetables that we grow on our farm located in Maine, USA.
Our products include:
1) a Traditional and Vegan Korean Kimchi
2) Barrow Glaze (a Korean Hot Sauce)
3) Pickle Parade Relish
4) Plumtastic Chutney
5) Seasonal Soups (many varieties, depending on what's available during the season)
6) Lone Pine Maple Syrup (we are retired from the U.S. Border Patrol, hence the name and spelling)
7) Kestrel Brook Kombucha (made with organic Maine wild blueberries)

For the Korean products (kimchi and barrow glaze) we would like to incorporate the Korean chili pepper (red) and chopsticks. The attached picture was taken from the internet, it has not been trademarked, but I am hesitant to use it as is as our business expands. Would like the "kimchi" to somehow incorporate the chopstick and pepper, but not look exactly like the attached image.

The final design should communicate farm fresh, organic, healthy and high quality ingredients, and Maine-made. All of our products go into glass jars 16oz and 8 oz. The hot sauce goes into 5.5oz and 8 oz bottles, the Maple Syrup goes into 8oz and 16oz bottles, and a 12oz bottle for the Kombucha. We will need the flexibility of changing some components of the label to accommodate each different food product.

The labels do not have the encircle the entirety of the jar. We understand that this is a tall order to fit so many different products. We are hoping that once we get the feel and design down, we can work with you for a fee outside of the competition to finalize other products labels on different sizes jars, bottles, etc. Its most important that we get the right feel for a label that can be used for a wide variety of food products.

Target Market(s)

Health conscious, foodies, local farm supporters

Font styles to use
Serif
Decorative
Script

Colors

Designer to choose colors to be used in the design.

Requirements
Must have
• Willow Ledge Farm Logo. Room for product name (interchangeable per product), ingredients list, space for jar size (8 oz, 12 oz, 16 oz). On Korean products -must have Korean hot chili pepper and chopsticks
Nice to have
• We'd like something fairly bold and rustic looking.
Should not have
• Nothing too modern or industrial looking. Nothing hippy-ish. Clean and professional. No cartoonish looking letters or designs.

```html
<!DOCTYPE html>
<html lang="en">
<head>
<meta charset="utf-8">
<title>Barrow Korean Hot Sauce – Label</title>
<link rel="stylesheet" href="https://fonts.googleapis.com/css2?family=Oswald:wght@500;600&family=Yellowtail&family=Open+Sans:wght@600&display=swap">
<style>
  :root {
    --page-bg: #ececec;
    --label-deep: #5e1616;
    --label-mid: #8a2420;
    --label-glow: #a9342b;
    --accent-yellow: #f4e233;
    --script-yellow: #f1e35c;
    --logo-cream: #efe9dc;
    --logo-ink: #2f4a66;
    --text-light: #f6efe4;
    --chili-red: #b3211b;
    --flame-orange: #e8923a;
  }
  html, body {
    margin: 0;
    width: 1200px;
    height: 800px;
    overflow: hidden;
    background: var(--page-bg);
  }
  .sheet {
    position: relative;
    width: 1200px;
    height: 800px;
  }
  .neck-band {
    position: absolute;
    left: 170px;
    top: 330px;
    width: 320px;
    height: 110px;
    background: radial-gradient(ellipse at center, var(--label-glow) 0%, var(--label-mid) 45%, var(--label-deep) 100%);
    display: flex;
    align-items: center;
    justify-content: center;
  }
  .neck-title {
    font-family: "Yellowtail", cursive;
    font-size: 54px;
    color: var(--script-yellow);
    letter-spacing: 1px;
  }
  .body-label {
    position: absolute;
    left: 600px;
    top: 50px;
    width: 400px;
    height: 700px;
    background: radial-gradient(ellipse at 50% 60%, var(--label-glow) 0%, var(--label-mid) 40%, var(--label-deep) 100%);
    display: flex;
    flex-direction: column;
    align-items: center;
    box-sizing: border-box;
    padding-top: 36px;
  }
  .farm-mark {
    display: flex;
    flex-direction: column;
    align-items: center;
    gap: 8px;
  }
  .farm-mark-circle {
    width: 64px;
    height: 64px;
    border-radius: 50%;
    background: var(--logo-cream);
  }
  .farm-mark-name {
    font-family: "Oswald", sans-serif;
    font-weight: 500;
    font-size: 22px;
    letter-spacing: 1px;
    color: var(--logo-cream);
    text-transform: uppercase;
  }
  .product-name {
    margin-top: 22px;
    font-family: "Oswald", sans-serif;
    font-weight: 600;
    font-size: 96px;
    line-height: 1;
    letter-spacing: 4px;
    color: var(--accent-yellow);
    position: relative;
  }
  .product-name sup {
    font-size: 14px;
    position: absolute;
    top: 4px;
    right: -14px;
    letter-spacing: 0;
  }
  .product-type {
    margin-top: 6px;
    font-family: "Yellowtail", cursive;
    font-size: 40px;
    color: var(--script-yellow);
  }
  .chili-art {
    margin-top: 22px;
    width: 300px;
    height: 250px;
    border-radius: 12px;
    background: radial-gradient(ellipse at 45% 55%, var(--flame-orange) 0%, var(--chili-red) 45%, rgba(94,22,22,0) 80%);
  }
  .net-weight {
    margin-top: auto;
    margin-bottom: 70px;
    font-family: "Open Sans", sans-serif;
    font-weight: 600;
    font-size: 18px;
    color: var(--text-light);
  }
</style>
</head>
<body>
  <main class="sheet">
    <section class="neck-band" aria-label="Neck label">
      <span class="neck-title">Hot Sauce</span>
    </section>

    <section class="body-label" aria-label="Front label">
      <div class="farm-mark">
        <span class="farm-mark-circle"></span>
        <span class="farm-mark-name">Willow Ledge Farm</span>
      </div>
      <h1 class="product-name">BARROW<sup>TM</sup></h1>
      <p class="product-type" style="margin-bottom:0">Korean Hot Sauce</p>
      <div class="chili-art" role="img" aria-label="Illustration of red Korean chili peppers in flames with a pair of chopsticks"></div>
      <p class="net-weight">Net Wt 16 oz (453g)</p>
    </section>
  </main>
</body>
</html>
```